Quorvel Business Card

I have a business that is called "Quorvel Electrical Products LTD" My company deals with top of the range laptops and mobile phones that are exclusive. I need a business card that will be eye catching but not over complicated.

Target Market(s)

Adults aged 19 to 50
Upper middle class

Industry/Entity Type

Business

Requirements
Must have
• Company name/logo (file attached)
• It must have my contact information which is:

• Name: Dale Marwick

• Position: Managing Director 

• Business Address: 7 Hapton Row, London, W4 9QD

• Contact Number: 02085193604
• Mobile: 07814260537
• Email: info@quorvel-goods.co.uk
Nice to have
• Simple and stylish
• Eye catching

```html
<!DOCTYPE html>
<html lang="en">
<head>
<meta charset="utf-8">
<title>Quorvel Electrical Products – Business Card</title>
<link rel="stylesheet" href="https://fonts.googleapis.com/css2?family=Source+Sans+3:wght@300;400;600;700&display=swap">
<style>
  :root {
    --paper: #ffffff;
    --brand-cyan: #3fb8d6;
    --brand-blue: #1f7fb0;
    --accent-orange: #d13f0c;
    --header-dark: #262b2d;
    --panel-grey: #7f8f8d;
    --divider: #72817f;
    --text-light: #e8ecea;
    --text-dark: #0b0b0b;
  }
  html, body {
    margin: 0;
    padding: 0;
    width: 1200px;
    height: 686px;
    overflow: hidden;
    background: var(--paper);
  }
  .card {
    position: relative;
    width: 1200px;
    height: 686px;
    overflow: hidden;
    background: var(--panel-grey);
    font-family: "Source Sans 3", "Myriad Pro", Arial, sans-serif;
  }
  .brand-strip {
    position: absolute;
    left: 0;
    top: 0;
    width: 171px;
    height: 686px;
    background: var(--paper);
  }
  .accent-band {
    position: absolute;
    left: 171px;
    top: 0;
    width: 69px;
    height: 686px;
    background: var(--accent-orange);
  }
  .brand-lettering {
    position: absolute;
    left: 0;
    top: 0;
  }
  .brand-name {
    font-family: "Source Sans 3", Arial, sans-serif;
    font-weight: 400;
    fill: var(--brand-cyan);
  }
  .brand-descriptor {
    font-family: "Source Sans 3", Arial, sans-serif;
    font-weight: 300;
    fill: var(--brand-blue);
  }
  .header-band {
    position: absolute;
    left: 240px;
    top: 0;
    width: 960px;
    height: 129px;
    background: var(--header-dark);
  }
  .person-name {
    position: absolute;
    left: 291px;
    top: 73px;
    margin: 0;
    font-size: 68px;
    font-weight: 700;
    line-height: 1;
    letter-spacing: 0.5px;
    color: var(--paper);
    text-transform: uppercase;
    white-space: nowrap;
  }
  .person-role {
    position: absolute;
    left: 291px;
    top: 147px;
    margin: 0;
    font-size: 49px;
    font-weight: 700;
    line-height: 1;
    color: var(--text-dark);
    white-space: nowrap;
  }
  .address {
    position: absolute;
    left: 291px;
    top: 230px;
    margin: 0;
    font-style: normal;
    font-size: 46px;
    font-weight: 400;
    line-height: 56px;
    color: var(--text-light);
    white-space: nowrap;
  }
  .divider {
    position: absolute;
    left: 240px;
    top: 437px;
    width: 960px;
    height: 1px;
    background: var(--divider);
  }
  .contact-list {
    position: absolute;
    left: 291px;
    top: 455px;
    margin: 0;
    padding: 0;
    list-style: none;
    font-size: 48px;
    font-weight: 400;
    line-height: 56px;
    color: var(--text-dark);
    white-space: nowrap;
  }
</style>
</head>
<body>
  <div class="card">
    <div class="brand-strip"></div>
    <div class="accent-band"></div>

    <svg class="brand-lettering" width="240" height="686" viewBox="0 0 240 686" aria-label="Quorvel Electrical Products">
      <text class="brand-name" transform="translate(152,594) rotate(-90)" font-size="150" textLength="548" lengthAdjust="spacingAndGlyphs">QUORVEL</text>
      <text class="brand-descriptor" transform="translate(222,594) rotate(-90)" font-size="50" textLength="543" lengthAdjust="spacingAndGlyphs">Electrical Products</text>
    </svg>

    <div class="header-band"></div>
    <h1 class="person-name">Dale Marwick</h1>
    <p class="person-role">Managing Director</p>

    <address class="address">
      7 Hapton Row<br>
      London<br>
      W4 9QD
    </address>

    <div class="divider"></div>

    <ul class="contact-list">
      <li>ph. 02085193604</li>
      <li>mobile. 07814260537</li>
      <li>info@quorvel-goods.co.uk</li>
    </ul>
  </div>
</body>
</html>
```